Design an Alcohol Bottle Wrapping (Medical Alcohol)

Looking to design a wrap of an Alcohol product for medical use.

Brand Name: VEMRI
Size: height : 11cm width: 14cm

Text on wrap and details are attached in the document

```html
<!DOCTYPE html>
<html lang="en">
<head>
<meta charset="utf-8">
<title>VEMRI Isopropyl Alcohol Wrap</title>
<link rel="stylesheet" href="https://fonts.googleapis.com/css2?family=Arimo:wght@400;700&family=Noto+Sans+Thai:wght@400;700&display=swap">
<style>
  :root {
    --wrap-red: #ee3c3c;
    --panel-white: #ffffff;
    --ink: #1a1a1a;
    --divider: #2b2b2b;
    --accent-red: #e3262b;
    --label-white: #ffffff;
  }
  html, body {
    margin: 0;
    padding: 0;
    overflow: hidden;
    background: var(--panel-white);
  }
  .wrap {
    position: relative;
    width: 1200px;
    height: 600px;
    overflow: hidden;
    font-family: "Arimo", "Noto Sans Thai", Arial, sans-serif;
    color: var(--ink);
  }
  .front-panel {
    position: absolute;
    left: 0;
    top: 0;
    width: 783px;
    height: 600px;
    background: var(--wrap-red);
  }
  .info-panel {
    position: absolute;
    left: 783px;
    top: 0;
    width: 417px;
    height: 600px;
    background: var(--panel-white);
  }
  .divider {
    position: absolute;
    left: 376px;
    top: 8px;
    width: 2px;
    height: 585px;
    background: var(--divider);
  }
  .english-copy {
    position: absolute;
    left: 40px;
    top: 40px;
    width: 300px;
    font-size: 15.5px;
    line-height: 22px;
  }
  .english-copy p {
    margin: 0 0 22px;
    text-align: justify;
  }
  .english-copy .line {
    display: block;
  }
  .brand-block {
    position: absolute;
    left: 414px;
    top: 68px;
    color: var(--label-white);
  }
  .brand-name {
    margin: 0;
    font-weight: 400;
    font-size: 82px;
    line-height: 1;
    letter-spacing: 1px;
  }
  .brand-sub {
    margin: 14px 0 0 2px;
    font-size: 25px;
    line-height: 1.2;
  }
  .thai-copy {
    position: absolute;
    left: 44px;
    top: 50px;
    width: 360px;
    font-family: "Noto Sans Thai", "Arimo", sans-serif;
    font-size: 15.5px;
    line-height: 22.5px;
  }
  .thai-copy p {
    margin: 0 0 22px;
  }
  .thai-copy .line {
    display: block;
  }
  .thai-copy .heading {
    color: var(--accent-red);
    font-weight: 700;
  }
</style>
</head>
<body>
<div class="wrap">
  <div class="front-panel">
    <div class="english-copy">
      <p>
        <span class="line">ALCOHOL</span>
        <span class="line">v/v %70 Isopropyl Alcohol</span>
      </p>
      <p>
        <span class="line">Alcohol</span>
        A topical antiseptic for disinfecting .wounds<br>
        Directions : Apply to wound area as necessary
      </p>
      <p>
        <span class="line">.using cotton pad or swab</span>
        <span class="line">For external use only</span>
        <span class="line">: Manufactured by</span>
        <span class="line">Kestrel Pharmacare Co.,Ltd</span>
        <span class="line">.</span>
        Rimnam Industrial ,4 Moo 58/12 Estate Ban Klang , Mueang Samut Thailand 74000 Sakhon, Samut Sakhon
      </p>
      <p>
        <span class="line">:Distributed by</span>
        <span class="line">Northwind Lab Co., LTD</span>
        212 ,905 Lotus Court Tower, Unit Sukhumvit Rd., Klongtoey, Bangkok .Thailand ,10110
      </p>
    </div>

    <div class="divider"></div>

    <div class="brand-block">
      <h1 class="brand-name">VEMRI</h1>
      <p class="brand-sub">Isopropyl Alcohol v/v %70</p>
    </div>
  </div>

  <div class="info-panel">
    <div class="thai-copy" lang="th">
      <p>
        <span class="line heading">แอลกอฮอล์</span>
        <span class="line">เอกสารกำกับยา</span>
        <span class="line">วิธีใช้: ใช้ล้างแผล</span>
        <span class="line">โดยใช้สำลีที่สะอาดชุบน้ำยาเช็ดบริเวณ</span>
      </p>
      <p>
        <span class="line heading">ที่เป็นแผล</span>
        <span class="line">คำเตือน : ยาใช้ภายนอกห้ามรับประทาน</span>
        <span class="line">30C การเก็บรักษา : เก็บที่อุณหภูมิ ไม่เกิน</span>
        <span class="line">มิลลิลิตร 30 : ขนาดบรรจุ</span>
        <span class="line">52/1A a17.Thai Reg. No</span>
      </p>
      <p>
        <span class="line">.Lot No</span>
        <span class="line">Mfg. Date</span>
        <span class="line">Exp. Date</span>
        <span class="line">(ยาสิ้นอายุ)</span>
      </p>
    </div>
  </div>
</div>
</body>
</html>
```